Modern luxury trendy cosmetics label

Looking for a cosmetics packaging label design. We are looking for a professionel, modern and luxury look like Lorena Vasquel, Meadowkin Apothecary, Marigold Tessin, Gavin Albert Pruke, Zuna, Orvik + Dalle, Velumi, Sleepy Walrus, the plainfold, lumiere de sable.Name of product: Nordic Tulip Mask - Needle-Free Contour Ritual Ingredients that have scientific proof of anti aging: Cherry blossom extact, collegen, hyaluronic acid, coconut oil. Color of product itself: Pastel pink. Smell: Cherry blossom. Colors of label: simple and black and white or some subtle colors.

Target Market(s)

Women, luxury market, modern women, young and old women

Industry/Entity Type

Cosmetics

Font styles to use
Sans Serif

Colors

Designer to choose colors to be used in the design.

Requirements
Must have
• A modern look, professional, cosmetics, beauty, professional market, original

```html
<!DOCTYPE html>
<html lang="en">
<head>
<meta charset="utf-8">
<title>Nordic Tulip Mask – Label</title>
<link rel="stylesheet" href="https://fonts.googleapis.com/css2?family=Abel&family=Great+Vibes&display=swap">
<style>
  :root {
    --backdrop: #ececee;
    --label-pink: #fde1e5;
    --blossom-white: #fff6f8;
    --blossom-pink: #f6c9d5;
    --panel-navy: #292d40;
    --ink-light: #ffffff;
    --ink-blush: #f7d6dc;
  }
  * { margin: 0; padding: 0; box-sizing: border-box; }
  html, body { width: 900px; height: 1200px; overflow: hidden; background: var(--backdrop); }
  .canvas { position: relative; width: 900px; height: 1200px; }
  .label {
    position: absolute; left: 90px; top: 38px; width: 720px; height: 1123px;
    background: var(--label-pink); overflow: hidden;
  }
  .blossom-area { position: absolute; }
  .blossom-top {
    right: 0; top: 0; width: 480px; height: 310px;
    background:
      radial-gradient(ellipse 90px 80px at 80px 80px, var(--blossom-white) 0%, rgba(255,246,248,0.5) 60%, transparent 100%),
      radial-gradient(ellipse 110px 100px at 330px 180px, var(--blossom-white) 0%, rgba(255,246,248,0.5) 60%, transparent 100%),
      radial-gradient(ellipse 90px 70px at 330px 40px, var(--blossom-white) 0%, rgba(255,246,248,0.4) 60%, transparent 100%),
      radial-gradient(ellipse 60px 60px at 220px 140px, var(--blossom-pink) 0%, transparent 100%);
    opacity: 0.9;
  }
  .blossom-bottom {
    left: 0; bottom: 0; width: 720px; height: 340px;
    background:
      radial-gradient(ellipse 150px 130px at 110px 200px, var(--blossom-white) 0%, rgba(255,246,248,0.5) 60%, transparent 100%),
      radial-gradient(ellipse 70px 60px at 40px 60px, var(--blossom-white) 0%, transparent 100%),
      radial-gradient(ellipse 100px 90px at 470px 100px, var(--blossom-white) 0%, rgba(255,246,248,0.4) 60%, transparent 100%),
      radial-gradient(ellipse 80px 60px at 400px 320px, var(--blossom-white) 0%, transparent 100%);
    opacity: 0.9;
  }
  .info-panel {
    position: absolute; left: 108px; top: 205px; width: 521px; height: 693px;
    background: var(--panel-navy);
  }
  .info-frame {
    position: absolute; left: 31px; top: 41px; right: 29px; bottom: 39px;
    border: 2px solid var(--ink-light);
  }
  .panel-text {
    position: absolute; left: 0; width: 100%; text-align: center;
    font-family: "Abel", sans-serif; color: var(--ink-light); line-height: 1;
  }
  .product-origin {
    top: 88px; font-family: "Great Vibes", cursive; font-size: 98px; color: var(--ink-blush);
  }
  .product-name { top: 205px; font-size: 40px; }
  .product-claim { top: 322px; font-size: 36px; line-height: 49px; }
  .scent {
    top: 507px; left: 125px; width: 253px; height: 57px;
    border-top: 2px solid var(--ink-light); border-bottom: 2px solid var(--ink-light);
    font-size: 29px; line-height: 53px; letter-spacing: 0.5px;
  }
  .volume { top: 596px; font-size: 24px; }
</style>
</head>
<body>
<main class="canvas">
  <section class="label">
    <div class="blossom-area blossom-top" role="img" aria-label="Soft white and pink cherry blossom flowers"></div>
    <div class="blossom-area blossom-bottom" role="img" aria-label="Soft white and pink cherry blossom flowers"></div>
    <div class="info-panel">
      <div class="info-frame"></div>
      <h1 class="panel-text product-origin">Nordic</h1>
      <p class="panel-text product-name">Tulip Mask</p>
      <p class="panel-text product-claim">Needle-Free<br>Contour Ritual</p>
      <p class="panel-text scent">CHERRY BLOSSOM</p>
      <p class="panel-text volume">10 FL. OZ / 300 mLe</p>
    </div>
  </section>
</main>
</body>
</html>
```